Email Marketing Campaign Templates

Email drip childcare campaign designed to communicate with parents interested in services. We would like the template(s) to be created so that we can change the content as needed.I will add below collateral that we have used in the past as well as logo.
three to for templates 1.) welcome template 2/ things to bring 3) generic template
Target Market(s)
Parents and Millennials
Industry/Entity Type
Childcare
Colors
85cae6
0493ce
9bcb3c
add136
fefefe
faa54b
cadf82
86cae7
33a6d7
Requirements
Must have
- Photos of staff with children
Nice to have
- Photos

```html
<!DOCTYPE html>
<html lang="en">
<head>
<meta charset="utf-8">
<title>Bloom Early Learning Center – Welcome Email</title>
<link rel="stylesheet" href="https://fonts.googleapis.com/css2?family=Courgette&family=Tinos&family=Open+Sans:ital,wght@1,700&display=swap">
<style>
  :root {
    --leaf-green: #72b843;
    --deep-blue: #0a6cc4;
    --brand-blue: #1e9bd7;
    --sun-orange: #f7b02b;
    --white: #fefefe;
  }
  * { margin: 0; padding: 0; box-sizing: border-box; }
  html, body { width: 1200px; height: 3013px; overflow: hidden; }
  body { background: var(--leaf-green); position: relative; font-family: "Tinos", serif; color: var(--white); }

  .hero {
    position: absolute; left: 0; top: 0; width: 1200px; height: 1130px;
    background:
      radial-gradient(circle at 14% 12%, rgba(255,255,255,0.95) 0, rgba(255,255,255,0.75) 14%, rgba(255,255,255,0) 30%),
      radial-gradient(ellipse at 78% 72%, #d8262c 0, #d8262c 16%, rgba(216,38,44,0) 34%),
      radial-gradient(ellipse at 36% 70%, #2f7fd0 0, #e8c23a 14%, rgba(232,194,58,0) 32%),
      radial-gradient(circle at 68% 10%, #8e4fc2 0, rgba(142,79,194,0) 22%),
      radial-gradient(circle at 92% 30%, #3aa3e0 0, rgba(58,163,224,0) 22%),
      radial-gradient(circle at 8% 55%, #f08a2a 0, rgba(240,138,42,0) 24%),
      radial-gradient(circle at 50% 28%, #f1d3b6 0, rgba(241,211,182,0) 26%),
      linear-gradient(160deg, #f6e7e9 0%, #ecc5b6 45%, #e7a86e 100%);
  }
  .hero-wave { position: absolute; left: 0; top: 960px; width: 1200px; height: 172px; }

  .brand {
    position: absolute; left: 60px; top: 70px;
    display: flex; align-items: center; gap: 20px;
  }
  .brand-dot { width: 72px; height: 72px; border-radius: 50%; background: var(--brand-blue); }
  .brand-name {
    font-family: "Courgette", cursive; font-size: 44px; line-height: 52px;
    color: var(--brand-blue); width: 290px;
  }

  .welcome-title {
    position: absolute; left: 0; top: 1160px; width: 1200px; text-align: center;
    font-family: "Courgette", cursive; font-weight: 400; font-size: 56px; line-height: 72px;
  }
  .welcome-text {
    position: absolute; left: 80px; top: 1318px; width: 1040px; text-align: center;
    font-size: 30px; line-height: 43px;
  }
  .read-more {
    position: absolute; left: 422px; top: 1486px; width: 328px; height: 90px;
    background: var(--sun-orange); display: flex; align-items: center; justify-content: center;
    font-family: "Open Sans", sans-serif; font-style: italic; font-weight: 700; font-size: 29px;
    color: var(--white); text-decoration: none;
  }

  .feature { position: absolute; width: 500px; text-align: center; }
  .feature-photo { width: 100%; height: 322px; }
  .feature-title {
    font-family: "Courgette", cursive; font-weight: 400; font-size: 44px; line-height: 56px; margin-top: 20px;
  }
  .feature-text { font-size: 29px; line-height: 39px; width: 490px; margin: 6px auto 0; }
  .feature--a { left: 70px; top: 1648px; }
  .feature--b { left: 630px; top: 1648px; }
  .feature--c { left: 70px; top: 2236px; }
  .feature--d { left: 630px; top: 2236px; }
  .photo-teacher { background: linear-gradient(120deg, #f1ece4, #8a5a3a 50%, #f2d3b3 80%, #7fc6e0); }
  .photo-snack { background: linear-gradient(120deg, #c7dff1, #e9c8a6 45%, #c43a3a 75%, #3a2e3e); }
  .photo-classroom { background: linear-gradient(120deg, #b48a5a, #3f6fa8 45%, #3d8a55 75%, #caa678); }
  .photo-paint { background: linear-gradient(120deg, #f4f1ea, #f0c34a 40%, #e9b48e 65%, #4a8fd3); }

  .footer-wave { position: absolute; left: 0; top: 2800px; width: 1200px; height: 70px; }
  .footer {
    position: absolute; left: 0; top: 2866px; width: 1200px; height: 147px;
    background: var(--deep-blue); display: flex; align-items: center; justify-content: center;
    font-size: 32px; letter-spacing: 1px;
  }
</style>
</head>
<body>
  <header>
    <div class="hero" role="img" aria-label="Photo of two smiling children lying among colourful toy blocks, holding blocks up to their eyes"></div>
    <svg class="hero-wave" viewBox="0 0 1200 172" preserveAspectRatio="none" aria-hidden="true">
      <path d="M0 166 C200 160 330 100 520 70 C700 44 820 24 980 44 C1080 56 1150 36 1200 24 L1200 172 L0 172 Z" fill="var(--leaf-green)"/>
    </svg>
    <div class="brand">
      <span class="brand-dot"></span>
      <span class="brand-name">Bloom Early Learning Center</span>
    </div>
  </header>

  <main>
    <h1 class="welcome-title">Welcome to our children &nbsp;at<br>bloom early learning center</h1>
    <p class="welcome-text">Lorem Ipsum is simply dummy text of the printing and typesetting industry. Lorem Ipsum has been the industry's standard dummy text ever since the 1500s, when an unknown printer took a galley</p>
    <a class="read-more" href="#">Read More..</a>

    <section class="feature feature--a">
      <div class="feature-photo photo-teacher" role="img" aria-label="Photo of a teacher showing a tablet to a toddler"></div>
      <h2 class="feature-title">Children Text here</h2>
      <p class="feature-text">Lorem Ipsum is simply dummy text of the printing and typesetting industry. Lorem Ipsum has been</p>
    </section>
    <section class="feature feature--b">
      <div class="feature-photo photo-snack" role="img" aria-label="Photo of two children enjoying a snack together"></div>
      <h2 class="feature-title">Children Text here</h2>
      <p class="feature-text">Lorem Ipsum is simply dummy text of the printing and typesetting industry. Lorem Ipsum has been</p>
    </section>
    <section class="feature feature--c">
      <div class="feature-photo photo-classroom" role="img" aria-label="Photo of children working at a classroom table"></div>
      <h2 class="feature-title">Children Text here</h2>
      <p class="feature-text">Lorem Ipsum is simply dummy text of the printing and typesetting industry. Lorem Ipsum has been</p>
    </section>
    <section class="feature feature--d">
      <div class="feature-photo photo-paint" role="img" aria-label="Photo of two excited children with painted hands"></div>
      <h2 class="feature-title">Children Text here</h2>
      <p class="feature-text">Lorem Ipsum is simply dummy text of the printing and typesetting industry. Lorem Ipsum has been</p>
    </section>
  </main>

  <svg class="footer-wave" viewBox="0 0 1200 70" preserveAspectRatio="none" aria-hidden="true">
    <path d="M0 30 C60 10 110 50 170 34 C240 14 290 52 360 36 C430 18 480 50 560 34 C640 16 690 52 770 36 C850 18 900 50 980 32 C1060 14 1110 48 1200 26 L1200 70 L0 70 Z" fill="var(--deep-blue)"/>
  </svg>
  <footer class="footer">Copyright@bloomearlylearning</footer>
</body>
</html>
```